RK Brennan & Associates

Create a website encompassing design work already carried out for business card.
Small accounting practice, business accounting and management, superannuation, audit, taxation.

```html
<!DOCTYPE html>
<html lang="en">
<head>
<meta charset="utf-8">
<title>RK Brennan &amp; Associates</title>
<link rel="stylesheet" href="https://fonts.googleapis.com/css2?family=Raleway:wght@300;400;500;600&family=Open+Sans:ital,wght@0,400;0,600;1,400&display=swap">
<style>
:root{
  --sky:#41a9e0;
  --navy:#1b4f86;
  --ink:#222;
  --grey-text:#6b6b6b;
  --pale:#efefef;
  --line:#e3e3e3;
  --white:#fff;
}
*{margin:0;padding:0;box-sizing:border-box}
html,body{width:821px;height:1200px;overflow:hidden;background:var(--white)}
body{position:relative;font-family:"Open Sans",sans-serif;color:var(--ink)}
.abs{position:absolute}
.wrap{position:absolute;left:122px;width:578px}

/* header */
.brand{left:162px;top:12px;display:flex;align-items:center;gap:8px}
.brand-mark{width:30px;height:30px;background:var(--sky)}
.brand-name{font-family:"Raleway",sans-serif;font-weight:600;font-size:15px;line-height:15px;color:var(--ink);width:110px}
.phone{right:123px;top:12px;font-size:8px;display:flex;align-items:center;gap:4px}
.social{display:flex;gap:6px}
.social span{width:13px;height:13px;border-radius:50%;display:block}
.social .c1{background:#3b5998}.social .c2{background:#1da1f2}.social .c3{background:#0a66c2}.social .c4{background:#cc2020}
.header-social{right:123px;top:31px}

/* nav */
.navbar{left:0;top:57px;width:821px;height:15px;background:var(--sky);color:var(--white)}
.tagline{position:absolute;left:122px;top:3px;font-size:5.3px;font-weight:600}
.menu{position:absolute;right:121px;top:2px;display:flex;font-size:7px;font-family:"Raleway",sans-serif;font-weight:500}
.menu span{padding:0 5px;border-left:1px solid rgba(255,255,255,.5)}
.menu span:first-child{border-left:none}

/* hero */
.hero{left:0;top:72px;width:821px;height:185px;background:linear-gradient(90deg,#f1f1f1 0%,#ececec 45%,#dcdcdc 60%,#c9ccd0 100%)}
.hero-photo{position:absolute;left:400px;top:0;width:300px;height:185px;background:linear-gradient(180deg,#d8dbe0,#b3b6ba 60%,#7c7f84)}
.hero-title{position:absolute;left:120px;top:66px;font-family:"Raleway",sans-serif;font-weight:400;font-size:23px;line-height:30px;color:#2a2a2a}
.dots{position:absolute;left:121px;top:164px;display:flex;gap:4px}
.dots span{width:7px;height:7px;border-radius:50%;border:1px solid #999;background:var(--white)}
.dots span:first-child{background:#999}

/* mission */
.mission{left:0;top:257px;width:821px;height:83px;background:var(--navy);color:var(--white)}
.mission h2{position:absolute;left:122px;top:9px;font-family:"Raleway",sans-serif;font-weight:400;font-size:13px}
.mission p{position:absolute;left:122px;top:28px;width:585px;font-size:7.6px;font-style:italic;line-height:16px}

/* welcome */
.welcome h1{position:absolute;left:0;top:358px;width:821px;text-align:center;font-family:"Raleway",sans-serif;font-weight:400;font-size:16px;line-height:21px}
.welcome p{position:absolute;left:120px;top:408px;width:581px;text-align:center;font-size:7.8px;line-height:16px;color:#444}
.divider{left:0;top:470px;width:821px;height:1px;background:var(--line)}

/* services */
.section-title{left:0;top:484px;width:821px;text-align:center;font-family:"Raleway",sans-serif;font-size:16px}
.service{position:absolute;width:180px;text-align:center}
.service svg{display:block;margin:0 auto;width:36px;height:36px}
.service h3{font-family:"Raleway",sans-serif;font-weight:400;font-size:12px;margin-top:6px}
.service p{font-size:7.6px;line-height:16px;color:var(--grey-text);margin-top:2px}
.service a{display:block;font-size:7.6px;color:var(--sky);text-decoration:none;margin-top:0;line-height:16px}
.view-all{left:597px;top:727px;font-family:"Raleway",sans-serif;font-size:12px;color:var(--sky);border-bottom:1px solid var(--sky);padding-bottom:1px}

/* cta */
.cta{left:0;top:802px;width:821px;height:40px;background:var(--sky)}
.cta h2{position:absolute;left:121px;top:12px;font-family:"Raleway",sans-serif;font-weight:400;font-size:14px;color:var(--white)}
.cta-btn{position:absolute;right:121px;top:10px;width:72px;height:20px;background:var(--white);color:var(--sky);font-size:8.5px;text-align:center;line-height:20px}

/* testimonial */
.testimonial{left:0;top:842px;width:821px;height:210px;background:var(--pale)}
.portrait{position:absolute;left:165px;top:62px;width:86px;height:86px;border-radius:50%;border:2px solid var(--white);background:radial-gradient(circle at 50% 40%,#d0d0d0,#8a8a8a)}
.quote{position:absolute;left:289px;top:66px;width:370px;font-size:12px;line-height:19.3px;color:#333}
.qmark{position:absolute;font-family:Georgia,serif;font-size:50px;color:#bbb;line-height:1}
.arrow{position:absolute;top:96px}

/* footer */
.foot-col{position:absolute;top:1062px;font-size:8px;color:#555}
.foot-col h4{font-weight:600;font-size:8.2px;color:#444;margin-bottom:6px}
.foot-col li{list-style:none;line-height:17px}
.field{width:116px;height:17px;border:1px solid #ccc;font-size:5.5px;color:#999;padding:4px 6px;margin-bottom:6px;background:var(--white)}
.signup{width:44px;height:16px;background:var(--sky);color:var(--white);font-size:7px;font-weight:600;text-align:center;line-height:16px}
.foot-line{left:122px;top:1160px;width:578px;height:1px;background:#ccc}
.copyright{left:0;top:1175px;width:821px;text-align:center;font-size:7.8px;color:#555}
</style>
</head>
<body>

<header>
  <div class="abs brand"><span class="brand-mark"></span><span class="brand-name">RK Brennan &amp; Associates</span></div>
  <div class="abs phone">
    <svg width="7" height="9" viewBox="0 0 7 9"><path d="M5 0.5C2 1 1 4 2.5 8.5" stroke="#41a9e0" stroke-width="1.8" fill="none" stroke-linecap="round"/></svg>
    +1 (123) 555 0142
  </div>
  <div class="abs social header-social"><span class="c1"></span><span class="c2"></span><span class="c3"></span><span class="c4"></span></div>
</header>

<nav class="abs navbar">
  <div class="tagline">Accountant · Business Solutions · Management · Superannuation · Audit</div>
  <div class="menu"><span>HOME</span><span>ABOUT US</span><span>SERVICES</span><span>LATEST NEWS</span><span>TESTIMONIALS</span><span>CONTACT US</span></div>
</nav>

<section class="abs hero">
  <div class="hero-photo" role="img" aria-label="Photograph of three business colleagues reviewing work on a laptop in a bright office"></div>
  <h1 class="hero-title">Business Management<br>For Your Business</h1>
  <div class="dots"><span></span><span></span><span></span></div>
</section>

<section class="abs mission">
  <h2>Our Mission</h2>
  <p>Lorem Ipsum is simply dummy text of the printing and typesetting industry. Lorem Ipsum has been the industry's standard dummy text ever since the 1500s, when an unknown printer took a galley of type and scrambled it to make a type specimen book. It has survived not only five centuries, but also the leap into electronic typesetting, remaining essentially unchanged. It was popularised in the 1960s with the release of Letraset sheets containing.</p>
</section>

<section class="welcome">
  <h1>Welcome to<br>RK Brennan &amp; Associates</h1>
  <p>Lorem Ipsum is simply dummy text of the printing and typesetting industry. Lorem Ipsum has been the industry's standard dummy text ever since the 1500s, when an unknown printer took a galley of type and scrambled it to make a type specimen book. It has survived not only five centuries, but also the leap into electronic typesetting, remaining essentially unchanged. It was popularised in the 1960s with the release of Letraset .</p>
</section>
<div class="abs divider"></div>

<h2 class="abs section-title">Services we offer</h2>

<div class="service" style="left:115px;top:524px">
  <svg viewBox="0 0 36 36" fill="none" stroke="#41a9e0" stroke-width="1.6"><path d="M9 30a7 7 0 0 1-1-14 10 10 0 0 1 19-2 7 7 0 0 1 1 16z"/><rect x="13" y="13" width="10" height="14" rx="1.5"/><path d="M15 16h6M15 20h1M18 20h1M21 20h0.5M15 23h1M18 23h1M21 23h0.5"/></svg>
  <h3>Accounting</h3>
  <p>Lorem Ipsum is simply dummy text of the printing and typesetting industry. Lorem Ipsum has been the industry's standard .</p>
  <a href="#">Click Here</a>
</div>
<div class="service" style="left:323px;top:524px">
  <svg viewBox="0 0 36 36" fill="none" stroke="#41a9e0" stroke-width="1.8" stroke-linejoin="round"><path d="M2 14l7-5 6 3M34 14l-7-5-8 4-5 4 2 2 5-3 7 7"/><path d="M5 15l8 9 3 1 8-1"/></svg>
  <h3>Business Management</h3>
  <p>Lorem Ipsum is simply dummy text of the printing and typesetting industry. Lorem Ipsum has been the industry's standard .</p>
  <a href="#">Click Here</a>
</div>
<div class="service" style="left:526px;top:524px">
  <svg viewBox="0 0 36 36" fill="none" stroke="#41a9e0" stroke-width="1.6"><rect x="7" y="5" width="20" height="26" rx="1.5"/><rect x="13" y="3" width="8" height="4" rx="1"/><path d="M11 13h12M11 17h12M11 21h8"/><circle cx="27" cy="27" r="5" fill="#41a9e0"/><path d="M24.5 27l2 2 3-3.5" stroke="#fff"/></svg>
  <h3>Audit</h3>
  <p>Lorem Ipsum is simply dummy text of the printing and typesetting industry. Lorem Ipsum has been the industry's standard .</p>
  <a href="#">Click Here</a>
</div>
<div class="service" style="left:115px;top:660px">
  <svg viewBox="0 0 36 36" fill="none" stroke="#41a9e0" stroke-width="1.8"><path d="M20 4H8v28h18V13"/><path d="M19 12c-4-2-7 0-5 3s6 2 5 6-5 3-7 1M16 9v3M16 22v3"/><path d="M26 4v8M23 7l3-3 3 3"/></svg>
  <h3>Superannuation</h3>
  <p>Lorem Ipsum is simply dummy text of the printing and typesetting industry. Lorem Ipsum has been the industry's standard .</p>
  <a href="#">Click Here</a>
</div>
<div class="service" style="left:323px;top:660px">
  <svg viewBox="0 0 36 36" fill="none" stroke="#41a9e0" stroke-width="1.8"><circle cx="11" cy="10" r="5"/><circle cx="25" cy="26" r="5"/><path d="M28 5L8 31"/></svg>
  <h3>Tax</h3>
  <p>Lorem Ipsum is simply dummy text of the printing and typesetting industry. Lorem Ipsum has been the industry's standard .</p>
  <a href="#">Click Here</a>
</div>
<div class="abs view-all">View all <svg width="7" height="8" viewBox="0 0 7 8"><path d="M1 1l5 3-5 3z" fill="#41a9e0"/></svg></div>

<section class="abs cta">
  <h2>Professional Accounting and Taxation Services</h2>
  <div class="cta-btn">CLICK HERE</div>
</section>

<section class="abs testimonial">
  <svg class="arrow" style="left:122px" width="12" height="18" viewBox="0 0 12 18"><path d="M10 2L3 9l7 7" stroke="#777" stroke-width="2.2" fill="none"/></svg>
  <div class="portrait" role="img" aria-label="Black and white portrait of a smiling client in a suit"></div>
  <div class="qmark" style="left:256px;top:52px">&ldquo;</div>
  <p class="quote">Lorem Ipsum is simply dummy text of the printing and typesetting industry. Lorem Ipsum has been the industry's standard dummy text ever since the 1500s, when an unknown printer took a galley of type and scrambled it to make a type specimen book.</p>
  <div class="qmark" style="left:596px;top:122px">&rdquo;</div>
  <svg class="arrow" style="left:687px" width="12" height="18" viewBox="0 0 12 18"><path d="M2 2l7 7-7 7" stroke="#777" stroke-width="2.2" fill="none"/></svg>
</section>

<footer>
  <div class="foot-col" style="left:122px"><h4>About</h4><ul><li>Home</li><li>About Us</li><li>Services</li><li>Latest News</li></ul></div>
  <div class="foot-col" style="left:229px"><h4>&nbsp;</h4><ul><li>Blogs</li><li>Downloads</li><li>Support</li><li>Partners</li></ul></div>
  <div class="foot-col" style="left:347px"><h4>Useful Links</h4><ul><li>Privacy Piolicy</li><li>Disclaimer</li><li>Contact us</li></ul></div>
  <div class="foot-col" style="left:463px"><h4>Subscribe to our Newsletter</h4><div class="field">Name</div><div class="field">Email Address</div><div class="signup">Sign Up</div></div>
  <div class="foot-col" style="left:625px"><h4>Social Media</h4><div class="social"><span class="c1"></span><span class="c2"></span><span class="c3"></span><span class="c4"></span></div></div>
  <div class="abs foot-line"></div>
  <div class="abs copyright">Copyright © 2014 RK Brennan &amp; Associates. All rights reserved.</div>
</footer>

</body>
</html>
```